BSWP Brightstep Foot Wellness Practice

Brightstep Foot Wellness Practice guarantees to treat your foot problems in one visit or we will provide a free treatment session to you until you are completely satisfied.

10% discount for all new patients!

Mobile foot care at home!

Professional and fully qualified and insured foot health care practitioner

Expert advice

How to care for your feet

Treatments; Diabetic foot health, Corns, Callouses, Fungal Infections, Verrucas, Cracked Heels, Ingrowing Toenails, Ball of foot pain and Heel pain.

Industry/Entity Type

Health Care

```html
<!DOCTYPE html>
<html lang="en">
<head>
<meta charset="utf-8">
<title>Brightstep Foot Wellness Practice – Flyers</title>
<link rel="stylesheet" href="https://fonts.googleapis.com/css2?family=Montserrat:wght@800;900&family=Nunito+Sans:wght@400;700;800&family=Tinos:wght@400;700&display=swap">
<style>
  :root {
    --backdrop: #6b5646;
    --paper: #ffffff;
    --ink: #111111;
    --red: #e0222e;
    --sky-top: #7e9fcf;
    --sky-bottom: #c9d8ea;
    --navy: #1c2a55;
    --skin: #c9a38a;
    --mono-light: #d8d8cf;
    --mono-dark: #4a4a44;
  }
  * { box-sizing: border-box; margin: 0; padding: 0; }
  html, body { width: 1200px; height: 1200px; overflow: hidden; }
  body {
    background: var(--backdrop);
    position: relative;
    font-family: "Nunito Sans", sans-serif;
    color: var(--ink);
  }
  .flyer {
    position: absolute;
    width: 540px;
    height: 780px;
    background: var(--paper);
    padding: 28px 30px;
    box-shadow: 0 6px 18px rgba(0,0,0,.35);
  }
  .flyer--offer { left: 30px; top: 210px; }
  .flyer--services { left: 630px; top: 210px; }

  /* masthead */
  .masthead { display: flex; align-items: center; gap: 18px; height: 128px; }
  .masthead__name {
    display: flex;
    align-items: center;
    gap: 12px;
    width: 276px;
  }
  .masthead__mark {
    flex: none;
    width: 22px;
    height: 22px;
    background: var(--red);
  }
  .masthead__title {
    font-family: "Montserrat", sans-serif;
    font-weight: 800;
    font-size: 36px;
    line-height: 1.05;
    letter-spacing: -.5px;
    color: var(--red);
  }
  .masthead__call { line-height: 1.05; }
  .masthead__call .call-now { font-family: "Montserrat", sans-serif; font-weight: 900; font-size: 32px; }
  .masthead__call .register { font-size: 28px; font-weight: 700; }
  .masthead__call .phone { font-size: 28px; font-weight: 700; letter-spacing: .5px; }
  .rule { height: 7px; background: var(--ink); margin: 10px 0 12px; }

  /* offer flyer */
  .headline {
    font-family: "Montserrat", sans-serif;
    font-weight: 900;
    font-size: 31px;
    line-height: 1.06;
    letter-spacing: -.6px;
    text-transform: uppercase;
  }
  .discount {
    font-family: "Montserrat", sans-serif;
    font-weight: 800;
    font-size: 23px;
    margin: 8px 0 10px;
  }
  .hero {
    position: relative;
    height: 432px;
    background: linear-gradient(180deg, var(--sky-top), var(--sky-bottom));
    font-family: "Tinos", serif;
  }
  .hero__photo {
    position: absolute;
    left: 180px; top: 110px; right: 0; bottom: 66px;
    background: radial-gradient(ellipse at 60% 45%, var(--skin), rgba(201,163,138,0) 70%);
  }
  .hero__guarantee {
    position: relative;
    padding: 12px 16px 0;
    color: var(--navy);
    font-size: 19px;
    line-height: 1.05;
  }
  .hero__guarantee .accent { color: #fff; }
  .hero__details {
    position: absolute;
    left: 20px; top: 118px;
    width: 150px;
    font-size: 14px;
    line-height: 1.3;
    color: var(--navy);
  }
  .hero__band {
    position: absolute;
    left: 0; right: 0; bottom: 0;
    height: 66px;
    background: var(--ink);
    color: #fff;
    padding: 10px 16px;
    font-size: 19px;
    line-height: 1.15;
    font-weight: 700;
  }

  /* services flyer */
  .feature { display: flex; gap: 12px; height: 216px; }
  .photo-pair { display: flex; gap: 8px; width: 300px; }
  .photo-pair .photo {
    flex: 1;
    position: relative;
    background: radial-gradient(ellipse at 50% 60%, #e8c6b3, #7a5a4c 80%);
  }
  .photo-pair .photo span {
    position: absolute; left: 0; right: 0; bottom: 70px;
    text-align: center; font-weight: 800; font-size: 15px;
  }
  .specialising {
    flex: 1;
    font-family: "Montserrat", sans-serif;
    font-weight: 900;
    font-size: 27px;
    line-height: 1.08;
    letter-spacing: -.5px;
  }
  .services { display: flex; gap: 14px; height: 326px; }
  .services__text { width: 290px; border-right: 4px solid var(--ink); padding-right: 12px; display: flex; flex-direction: column; }
  .off {
    font-family: "Montserrat", sans-serif;
    font-weight: 900;
    font-size: 58px;
    line-height: .95;
    letter-spacing: -1px;
  }
  .treatments { font-size: 36px; font-weight: 400; line-height: 1; letter-spacing: .5px; margin-bottom: 8px; }
  .treatment-list { font-size: 19px; line-height: 1.25; }
  .booking { margin-top: auto; font-weight: 800; font-size: 18px; line-height: 1.25; }
  .booking .practice { color: var(--red); font-size: 22px; }
  .booking .credential { font-size: 12px; font-weight: 700; }
  .photo-stack { flex: 1; display: flex; flex-direction: column; gap: 8px; }
  .photo-stack .photo {
    flex: 1;
    background: linear-gradient(135deg, var(--mono-light), var(--mono-dark));
  }
</style>
</head>
<body>

<article class="flyer flyer--offer">
  <header class="masthead">
    <div class="masthead__name">
      <span class="masthead__mark"></span>
      <div class="masthead__title">Brightstep Bulletin</div>
    </div>
    <div class="masthead__call">
      <div class="call-now">CALL NOW</div>
      <div class="register">to register</div>
      <div class="phone">07700900461</div>
    </div>
  </header>
  <div class="rule"></div>
  <h1 class="headline">Newly arrived mobile foot care at home now available in your area</h1>
  <p class="discount">10% Discounts for all new patients</p>
  <section class="hero">
    <div class="hero__photo" role="img" aria-label="Photo of a bare foot in a sandal raised against a blue sky"></div>
    <p class="hero__guarantee">BSWP Brightstep Foot Wellness Practice Guarantees to treat your foot problems in one visit or we will provide a <span class="accent">free treatment session</span> to you until you're completely satisfied.</p>
    <p class="hero__details">From as little as £30 per treatment session our fully qualified and insured Foot Health Care Practitioner will immediately bring you pain relief while also offering you professional expert advice on how to care for your feet and keep them looking good all year round.</p>
    <p class="hero__band">We will conveniently visit you in your own home or place of work which ever you find more comfortable.</p>
  </section>
</article>

<article class="flyer flyer--services">
  <header class="masthead">
    <div class="masthead__name">
      <span class="masthead__mark"></span>
      <div class="masthead__title">Brightstep Bulletin</div>
    </div>
    <div class="masthead__call">
      <div class="call-now">CALL NOW</div>
      <div class="register">to register</div>
      <div class="phone">07700900461</div>
    </div>
  </header>
  <div class="rule"></div>
  <section class="feature">
    <div class="photo-pair">
      <div class="photo" role="img" aria-label="Photo of a cracked heel before treatment"><span>Before</span></div>
      <div class="photo" role="img" aria-label="Photo of a smooth heel after treatment"><span>After</span></div>
    </div>
    <h2 class="specialising">Specialising in Diabetic foot health and Elderly foot care</h2>
  </section>
  <div class="rule"></div>
  <section class="services">
    <div class="services__text">
      <div class="off">10% OFF</div>
      <div class="treatments">TREATMENTS</div>
      <p class="treatment-list">Corns, Calluses, Fungal infections, Verrucas, Cracked heels, In-growing toenails, Ball of foot pain, Heel pain and Diabetic Foot Health.</p>
      <p class="booking">Call NOW!!! 07700900461<br>to book an appointment<br>with <span class="practice">BSWP</span> Ms R J Hale<br><span class="credential">DipCFHP Foot Health Care Practitioner</span></p>
    </div>
    <div class="photo-stack">
      <div class="photo" role="img" aria-label="Black and white photo of a practitioner's gloved hands treating toes"></div>
      <div class="photo" role="img" aria-label="Black and white photo of gloved hands examining the sole of a foot"></div>
      <div class="photo" role="img" aria-label="Black and white photo of a foot care treatment with instruments"></div>
    </div>
  </section>
</article>

</body>
</html>
```